Maple Ledger Business Card

Colors can be blue, grey and white as you see in the attached logo. Needs to have a spot for name, title, phone, email, address, and website. There also needs to be a spot for an agent's picture.

Contact Information for Business Card

See project description.

Colors

Designer to choose colors to be used in the design.

```html
<!DOCTYPE html>
<html lang="en">
<head>
<meta charset="utf-8">
<title>Maple Ledger Real Estate – Business Card</title>
<link href="https://fonts.googleapis.com/css2?family=Montserrat:wght@500;700&family=Lora:ital,wght@0,400;1,400&family=Roboto:wght@400&display=swap" rel="stylesheet">
<style>
  :root {
    --brand-blue: #2f6fb7;
    --ink: #2b2b2b;
    --card-white: #ffffff;
    --panel-grey: #f1f1f1;
    --canvas: #e6e6e6;
    --photo-dark: #3a2c26;
    --photo-light: #d9cfc8;
  }
  * { box-sizing: border-box; margin: 0; padding: 0; }
  html, body { width: 1200px; height: 924px; overflow: hidden; }
  body { background: var(--canvas); position: relative; }

  .card {
    position: absolute;
    width: 525px;
    height: 300px;
    background: var(--card-white);
    box-shadow: 0 6px 18px rgba(0,0,0,.18);
    overflow: hidden;
  }
  .card-front { left: 337px; top: 100px; background: #f5f5f5; }
  .card-back  { left: 337px; top: 500px; }

  /* brand lockup */
  .brand { position: absolute; text-align: center; font-family: "Montserrat", sans-serif; }
  .brand-row { display: flex; align-items: center; justify-content: center; gap: 8px; }
  .brand-dot { border-radius: 50%; background: var(--ink); }
  .brand-name { color: var(--brand-blue); font-weight: 700; white-space: nowrap; }
  .brand-sub {
    display: flex; align-items: center; gap: 6px; justify-content: center;
    color: var(--ink); font-weight: 500; letter-spacing: .25em;
  }
  .brand-sub::before, .brand-sub::after { content: ""; height: 1px; background: var(--ink); flex: 1; }

  .card-front .brand { left: 112px; top: 104px; width: 300px; }
  .card-front .brand-dot { width: 16px; height: 16px; }
  .card-front .brand-name { font-size: 30px; }
  .card-front .brand-sub { font-size: 10px; margin-top: 4px; }

  .social-dots { position: absolute; left: 0; right: 0; top: 196px; display: flex; justify-content: center; gap: 8px; }
  .social-dots span { width: 20px; height: 20px; border-radius: 50%; background: var(--brand-blue); }

  /* back */
  .back-shapes { position: absolute; inset: 0; }
  .agent-photo {
    position: absolute; left: 75px; top: 0; width: 190px; height: 262px;
    background: linear-gradient(180deg, var(--photo-light) 0%, #8a6a58 35%, var(--photo-dark) 100%);
  }
  .agent-name {
    position: absolute; left: 22px; top: 214px;
    font-family: "Lora", serif; font-size: 22px; color: #fff;
  }
  .agent-title {
    position: absolute; left: 150px; top: 244px;
    font-family: "Roboto", sans-serif; font-size: 11px; color: #dfe9f6;
  }
  .card-back .brand { right: 28px; top: 30px; width: 170px; }
  .card-back .brand-dot { width: 10px; height: 10px; }
  .card-back .brand-name { font-size: 17px; }
  .card-back .brand-sub { font-size: 6px; margin-top: 2px; }

  .contact-list {
    position: absolute; right: 16px; top: 92px; list-style: none;
    font-family: "Lora", serif; font-size: 12.5px; color: var(--ink); text-align: right;
  }
  .contact-list li { display: flex; justify-content: flex-end; align-items: center; gap: 10px; height: 18px; }
  .contact-list li.gap { margin-top: 6px; }
  .contact-list svg { width: 10px; height: 10px; fill: var(--brand-blue); flex: none; }
  .contact-list .no-icon::after { content: ""; width: 10px; flex: none; }
  .social-handles {
    position: absolute; left: 300px; top: 267px;
    font-family: "Lora", serif; font-style: italic; font-size: 11px; color: #fff;
  }
</style>
</head>
<body>

<section class="card card-front" aria-label="Card front">
  <div class="brand">
    <div class="brand-row"><span class="brand-dot"></span><span class="brand-name">Maple Ledger</span></div>
    <div class="brand-sub">REAL ESTATE</div>
  </div>
  <div class="social-dots"><span></span><span></span><span></span><span></span></div>
</section>

<section class="card card-back" aria-label="Card back">
  <svg class="back-shapes" viewBox="0 0 525 300" width="525" height="300">
    <polygon points="235,300 525,45 525,300" fill="#f1f1f1"/>
  </svg>
  <div class="agent-photo" role="img" aria-label="Portrait photo of the agent"></div>
  <svg class="back-shapes" viewBox="0 0 525 300" width="525" height="300">
    <polygon points="0,210 305,210 290,262 0,262" fill="#2f6fb7"/>
    <polygon points="290,262 500,262 492,292 282,292" fill="#2b2b2b"/>
  </svg>
  <div class="agent-name">Marisol Vance</div>
  <div class="agent-title">Relator Agent</div>

  <div class="brand">
    <div class="brand-row"><span class="brand-dot"></span><span class="brand-name">Maple Ledger</span></div>
    <div class="brand-sub">REAL ESTATE</div>
  </div>

  <ul class="contact-list">
    <li>800-555-0142 <svg viewBox="0 0 10 10"><path d="M2 0l2 2-1 1.5c.8 1.5 2 2.7 3.5 3.5L8 6l2 2-1.5 2C4 9.5.5 6 0 1.5z"/></svg></li>
    <li>800-555-0187 <svg viewBox="0 0 10 10"><rect x="0" y="3" width="10" height="7" rx="1"/><rect x="2" y="0" width="6" height="3"/></svg></li>
    <li class="gap">marisol@mapleledger.com <svg viewBox="0 0 10 10"><path d="M0 2h10v1L5 6 0 3zM0 4l5 3 5-3v4H0z"/></svg></li>
    <li>www.mapleledger.com <svg viewBox="0 0 10 10"><circle cx="5" cy="5" r="5"/></svg></li>
    <li class="gap">48 Birch Lane, Suite 5 <svg viewBox="0 0 10 10"><path d="M5 0a3.5 3.5 0 0 1 3.5 3.5C8.5 6 5 10 5 10S1.5 6 1.5 3.5A3.5 3.5 0 0 1 5 0zm0 2a1.5 1.5 0 1 0 0 3 1.5 1.5 0 0 0 0-3z"/></svg></li>
    <li class="no-icon">Dayton, US 45402</li>
  </ul>
  <div class="social-handles">@marisolvance.homes, @marisolvance</div>
</section>

</body>
</html>
```